Driftwater

Club flyer, grand opening night, house/electronic music, looking for clean design with a sample image attached. Please look at the prior flyers to get an idea of the style. Guaranteed project
I would like to use the red design if possible (driftwater flyer attached)
Text:
DRIFTWATER
Winter House Music Monthly
Opening Night Dec 13 2013
Tessaline (use logo)
Featuring
BRONTIK (House/Garage)
(use logo with just Brontik name)
w/ resident
ZEV (Pinwheel)
Free All Night
Target Market(s)
21-39 year old club with all house/electronic music. classier and grown up over gimmicky
Industry/Entity Type
Club
Look and feel

```html
<!DOCTYPE html>
<html lang="en">
<head>
<meta charset="utf-8">
<title>Driftwater — Winter House Music Monthly</title>
<link rel="stylesheet" href="https://fonts.googleapis.com/css2?family=Roboto+Condensed:wght@400;700;900&display=swap">
<style>
  :root {
    --flyer-pink: #ff1481;
    --burst-core: #ffffff;
    --burst-mid: #ff8cc4;
    --ink: #ffffff;
  }
  html, body {
    margin: 0;
    padding: 0;
    width: 1200px;
    height: 1200px;
    overflow: hidden;
    background: var(--flyer-pink);
  }
  .flyer {
    position: relative;
    width: 1200px;
    height: 1200px;
    background: var(--flyer-pink);
    color: var(--ink);
    font-family: "Roboto Condensed", "Arial Narrow", sans-serif;
    overflow: hidden;
  }
  .flyer > * {
    position: absolute;
    margin: 0;
    line-height: 1;
    white-space: nowrap;
  }
  .burst-art {
    left: 132px;
    top: 132px;
    width: 912px;
    height: 912px;
  }
  .venue-name {
    left: 24px;
    top: 36px;
    width: 330px;
    height: 156px;
    display: flex;
    align-items: center;
    justify-content: center;
    font-size: 46px;
    font-weight: 400;
    letter-spacing: 1px;
  }
  .event-title {
    right: 46px;
    top: 24px;
    font-size: 106px;
    font-weight: 700;
    letter-spacing: -1px;
  }
  .event-meta {
    right: 46px;
    font-size: 31px;
    font-weight: 400;
    text-align: right;
  }
  .event-meta--series { top: 126px; }
  .event-meta--date { top: 200px; }
  .lineup-label {
    left: 34px;
    font-size: 41px;
    font-weight: 400;
  }
  .lineup-label--featuring { top: 877px; }
  .lineup-label--resident { top: 1043px; }
  .headliner {
    left: 32px;
    top: 919px;
    font-size: 84px;
    font-weight: 900;
    letter-spacing: 2px;
  }
  .resident {
    left: 34px;
    top: 1077px;
    font-size: 96px;
    font-weight: 900;
  }
  .resident-crew {
    left: 222px;
    top: 1127px;
    font-size: 30px;
    font-weight: 700;
    letter-spacing: 2px;
    text-transform: uppercase;
  }
  .admission {
    right: 46px;
    top: 1120px;
    font-size: 38px;
    font-weight: 700;
  }
</style>
</head>
<body>
  <main class="flyer">
    <svg class="burst-art" viewBox="0 0 912 912" role="img" aria-label="Radiating white and pink kaleidoscope starburst pattern">
      <defs>
        <radialGradient id="burstGlow" cx="50%" cy="50%" r="50%">
          <stop offset="0%" stop-color="var(--burst-core)" stop-opacity="1"/>
          <stop offset="30%" stop-color="var(--burst-core)" stop-opacity="0.95"/>
          <stop offset="60%" stop-color="var(--burst-mid)" stop-opacity="0.75"/>
          <stop offset="100%" stop-color="var(--flyer-pink)" stop-opacity="0"/>
        </radialGradient>
      </defs>
      <circle cx="456" cy="456" r="456" fill="url(#burstGlow)"/>
    </svg>

    <p class="venue-name">TESSALINE</p>

    <h1 class="event-title">DRIFTWATER</h1>
    <p class="event-meta event-meta--series">Winter House Music Monthly</p>
    <p class="event-meta event-meta--date">Opening Night Dec 13 2013</p>

    <p class="lineup-label lineup-label--featuring">Featuring</p>
    <p class="headliner">BRONTIK</p>

    <p class="lineup-label lineup-label--resident">W/Resident</p>
    <p class="resident">ZEV</p>
    <p class="resident-crew">Pinwheel</p>

    <p class="admission">Free All Night</p>
  </main>
</body>
</html>
```